Design for a Service-Based Estimate

We want a design for an Estimate that will always be sent in PDF format. The estimate or proposal is a critical document that needs to plainly show the service items, item description but also needs to be attractive and professional looking. Our current estimate deliverable is attached but it looks really basic like a Word document

```html
<!DOCTYPE html>
<html lang="en">
<head>
<meta charset="utf-8">
<title>Firmline Pave Estimate – Page 2</title>
<link rel="stylesheet" href="https://fonts.googleapis.com/css2?family=Poppins:wght@400;500;600;700;800&display=swap">
<style>
  :root{
    --red:#e8352a;
    --navy:#2f2f4f;
    --ink:#2b2b3a;
    --rule:#c9c9cf;
    --canvas:#e9e9ec;
    --paper:#ffffff;
  }
  *{box-sizing:border-box;margin:0;padding:0}
  html,body{width:1200px;height:1200px;overflow:hidden;background:var(--canvas);font-family:'Poppins',sans-serif;color:var(--ink)}
  .sheet{position:absolute;left:175px;top:50px;width:850px;height:1100px;background:var(--paper);box-shadow:0 6px 24px rgba(0,0,0,.12);overflow:hidden}
  .corner-mark{position:absolute;left:0;top:44px;width:48px;height:48px;background:var(--red)}
  .brand{position:absolute;left:70px;top:50px;font-size:34px;font-weight:800;letter-spacing:1px;color:var(--navy);line-height:1}
  .doc-meta{position:absolute;right:0;top:0;width:420px;height:62px;background:var(--red);color:#fff;font-size:11px;font-weight:500;display:flex;align-items:center;padding-left:60px;gap:10px;clip-path:polygon(12% 0,100% 0,100% 100%,0 100%)}
  .section-title{position:absolute;left:70px;top:128px;width:710px;font-size:17px;font-weight:600;padding-bottom:8px;border-bottom:1px solid var(--rule)}
  .section-title small{font-size:12px;font-weight:500}
  .terms{position:absolute;left:70px;top:182px;width:710px;list-style:none;font-size:12.5px;line-height:1.55}
  .terms li{display:flex;gap:22px;margin-bottom:12px}
  .terms .num{flex:0 0 14px;font-weight:500}
  .sign-block{position:absolute;top:470px;width:300px}
  .sign-block.client{left:70px}
  .sign-block.date{left:520px;top:440px;width:260px}
  .sign-area{height:70px;margin:0 20px 6px;background:linear-gradient(90deg,rgba(43,43,58,.04),rgba(43,43,58,.08));border-radius:4px}
  .sign-line{border-top:1px solid var(--rule);padding-top:10px;font-size:15px;font-weight:600}
  .footer{position:absolute;left:0;bottom:70px;width:850px;height:76px;background:var(--navy);color:#fff;display:flex;align-items:center;justify-content:space-between;padding:0 40px;font-size:12px;line-height:1.5}
  .footer-item{display:flex;align-items:center;gap:12px}
  .icon{flex:0 0 28px;width:28px;height:28px;border-radius:50%;background:var(--red);display:flex;align-items:center;justify-content:center}
</style>
</head>
<body>
<main class="sheet">
  <div class="corner-mark"></div>
  <div class="brand">FIRMLINE PAVE</div>
  <div class="doc-meta"><span>Bid# 01245</span><span>|</span><span>Date 14th January 2021</span><span>|</span><span>PG No: 02</span></div>

  <h2 class="section-title">Terms &amp; Conditions <small>(contd.)</small></h2>
  <ol class="terms">
    <li><span class="num">5.</span><span>It is agreed by the Contractor and the Client that complications and costs arising from unforeseen conditions and handling of unsuitable materials are not included in this estimate.</span></li>
    <li><span class="num">6.</span><span>Unless specifically listed in this estimate, the following items and their costs are not included: Maintenance of Traffic, Concrete Material Pumping, Testing, Excavation, Grading and Fill Material, Permits and fees, Surveying and As-builts, Irrigation Repair, Landscaping and Root Migration, De-watering, Private Locates and Accessibility.</span></li>
    <li><span class="num">7.</span><span>Private utility locating services using radio detection devices and, when necessary, ground penetrating radar are offered by Firmline Pave to assist in finding private utilities that may not have been located by the public one call system. Firmline Pave will not be responsible for private utilities that have not been located nor for the failure of the above equipment to accurately detect existing utilities since the equipment is not infallible and existing site conditions may preclude the ability of the equipment to detect an identifiable signal.</span></li>
  </ol>

  <div class="sign-block client">
    <div class="sign-area" role="img" aria-label="Handwritten client signature"></div>
    <div class="sign-line">Client Signature</div>
  </div>
  <div class="sign-block date">
    <div class="sign-area"></div>
    <div class="sign-line">Date</div>
  </div>

  <footer class="footer">
    <div class="footer-item">
      <span class="icon"><svg width="14" height="14" viewBox="0 0 24 24"><path fill="#fff" d="M12 2a7 7 0 0 0-7 7c0 5 7 13 7 13s7-8 7-13a7 7 0 0 0-7-7zm0 9.5A2.5 2.5 0 1 1 12 6.5a2.5 2.5 0 0 1 0 5z"/></svg></span>
      <span>Lee (LIC00-00412, LIC00-00538) | Collier (LCC00-2207)<br>Cape Coral (#00417) | Charlotte (AAA-00-00291)</span>
    </div>
    <div class="footer-item">
      <span class="icon"><svg width="14" height="14" viewBox="0 0 24 24" fill="none" stroke="#fff" stroke-width="2"><circle cx="12" cy="12" r="9"/><path d="M3 12h18M12 3c3 3 3 15 0 18M12 3c-3 3-3 15 0 18"/></svg></span>
      <span>info@firmlinepave.com<br>www.firmlinepave.com</span>
    </div>
    <div class="footer-item">
      <span class="icon"><svg width="14" height="14" viewBox="0 0 24 24"><path fill="#fff" d="M6.6 10.8a15 15 0 0 0 6.6 6.6l2.2-2.2c.3-.3.7-.4 1-.2 1.1.4 2.3.6 3.6.6.6 0 1 .4 1 1V20c0 .6-.4 1-1 1A17 17 0 0 1 3 4c0-.6.4-1 1-1h3.5c.6 0 1 .4 1 1 0 1.3.2 2.5.6 3.6.1.3 0 .7-.2 1z"/></svg></span>
      <span>(555) 014-2270</span>
    </div>
  </footer>
</main>
</body>
</html>
```